Business card design for IT consulting company

Looking for a simple, modern, clean business card design.
Open to reworking our existing logo.

Attached is our current business cards which we do not like.
Ideally double sided with something simple on the back.
Rectangle / Horizonal only.
No rounded edges on the card.
White as the dominate color is preferred.

Target Market(s)

clients, legal, oil & gas, medical, professionals

Industry/Entity Type

IT, tech, consulting

Contact Information for Business Card

Name, Title, email, phone, cell, website

Font styles to use
Sans Serif

Requirements
Must have
• Clean design
Should not have
• loud colors or unusual fonts, etc

```html
<!DOCTYPE html>
<html lang="en">
<head>
<meta charset="utf-8">
<title>Norvik Solutions – Business Card</title>
<link rel="stylesheet" href="https://fonts.googleapis.com/css2?family=Montserrat:wght@600;700&family=Lato:wght@300;400&display=swap">
<style>
  :root {
    --backdrop: #6f7377;
    --card: #ffffff;
    --card-shade: #f1f1f2;
    --ink: #232a3b;
    --red: #e2404f;
    --blue: #48a8db;
    --accent-line: #16a2e0;
  }
  * { box-sizing: border-box; margin: 0; padding: 0; }
  html, body { width: 1200px; height: 892px; overflow: hidden; }
  body {
    background: var(--backdrop);
    display: flex;
    align-items: center;
    justify-content: center;
    gap: 60px;
    font-family: "Lato", Arial, sans-serif;
    color: var(--ink);
  }
  .card {
    position: relative;
    width: 520px;
    height: 297px;
    background: linear-gradient(135deg, var(--card) 55%, var(--card-shade));
    box-shadow: 0 18px 40px rgba(0,0,0,0.28);
    overflow: hidden;
  }

  .corner-accent {
    position: absolute;
    width: 150px;
    height: 90px;
    background: linear-gradient(135deg, var(--red), var(--blue));
  }
  .corner-accent--top-left {
    left: 0; top: 0;
    clip-path: polygon(0 0, 100% 0, 0 100%);
  }
  .corner-accent--bottom-right {
    right: 0; bottom: 0;
    clip-path: polygon(100% 0, 100% 100%, 0 100%);
  }

  .brand {
    display: flex;
    align-items: center;
    font-family: "Montserrat", Arial, sans-serif;
    font-weight: 700;
    color: var(--ink);
    letter-spacing: 0.12em;
    text-transform: uppercase;
  }
  .brand__square { background: var(--blue); flex: none; }

  .card--front .brand {
    position: absolute;
    left: 50%; top: 50%;
    transform: translate(-50%, -50%);
    flex-direction: column;
    gap: 12px;
    font-size: 17px;
    text-align: center;
    line-height: 1.25;
  }
  .card--front .brand__square { width: 44px; height: 44px; }

  .card--back .brand {
    position: absolute;
    right: 34px; top: 30px;
    flex-direction: column;
    gap: 10px;
    font-size: 14px;
    text-align: center;
    line-height: 1.25;
  }
  .card--back .brand__square { width: 40px; height: 40px; }

  .person { position: absolute; left: 34px; top: 66px; width: 240px; }
  .person__name {
    font-family: "Montserrat", Arial, sans-serif;
    font-weight: 700;
    font-size: 25px;
    letter-spacing: 0.01em;
    white-space: nowrap;
  }
  .person__title { font-weight: 300; font-size: 15px; margin-top: 2px; }
  .person__rule {
    position: relative;
    height: 2px;
    background: var(--ink);
    margin-top: 6px;
  }
  .person__rule::after {
    content: "";
    position: absolute;
    left: 0; top: 5px;
    width: 48px; height: 4px;
    background: var(--accent-line);
  }

  .contacts { position: absolute; left: 34px; top: 164px; list-style: none; }
  .contacts__row { display: flex; align-items: center; gap: 10px; margin-bottom: 12px; }
  .contacts__icon { width: 18px; height: 18px; flex: none; }
  .contacts__divider { width: 1.5px; height: 34px; background: var(--ink); flex: none; }
  .contacts__row--web .contacts__divider { background: var(--accent-line); }
  .contacts__lines { font-size: 15px; line-height: 1.2; white-space: nowrap; }
</style>
</head>
<body>

  <section class="card card--front" aria-label="Card front">
    <div class="corner-accent corner-accent--top-left" role="img" aria-label="Decorative corner accent in red and blue"></div>
    <div class="corner-accent corner-accent--bottom-right" role="img" aria-label="Decorative corner accent in red and blue"></div>
    <div class="brand">
      <span class="brand__square"></span>
      <span class="brand__name">Norvik<br>Solutions</span>
    </div>
  </section>

  <section class="card card--back" aria-label="Card back">
    <div class="corner-accent corner-accent--bottom-right" role="img" aria-label="Decorative corner accent in red and blue"></div>

    <div class="person">
      <h1 class="person__name">Daniel Moreau</h1>
      <p class="person__title">IT Consultant</p>
      <div class="person__rule"></div>
    </div>

    <ul class="contacts">
      <li class="contacts__row contacts__row--phone">
        <svg class="contacts__icon" viewBox="0 0 24 24" aria-label="Phone">
          <path fill="var(--accent-line)" d="M6.6 10.8a15.1 15.1 0 0 0 6.6 6.6l2.2-2.2c.3-.3.7-.4 1-.2 1.1.4 2.3.6 3.6.6.6 0 1 .4 1 1V20c0 .6-.4 1-1 1A17 17 0 0 1 3 4c0-.6.4-1 1-1h3.5c.6 0 1 .4 1 1 0 1.3.2 2.5.6 3.6.1.3 0 .7-.2 1z"/>
        </svg>
        <span class="contacts__divider"></span>
        <span class="contacts__lines">(555) 010-2468<br>(555) 014-7390</span>
      </li>
      <li class="contacts__row contacts__row--web">
        <svg class="contacts__icon" viewBox="0 0 24 24" aria-label="Email and web">
          <path fill="var(--ink)" d="M2 12 22 3l-6 18-4-7z"/>
        </svg>
        <span class="contacts__divider"></span>
        <span class="contacts__lines">daniel.moreau@norvik.ca<br>www.norvik.ca</span>
      </li>
    </ul>

    <div class="brand">
      <span class="brand__square"></span>
      <span class="brand__name">Norvik<br>Solutions</span>
    </div>
  </section>

</body>
</html>
```